A4 Menu needed for cafe - attached design

Need an A4 menu designed for our cafe.
I have attached our catering menu - I would like the new menu to be designed in the exact same way.

I have attached the text that needs to appear on the menu

```html
<!DOCTYPE html>
<html lang="en">
<head>
<meta charset="utf-8">
<title>Harbour Lane Canteen – Catering Menu</title>
<link rel="stylesheet" href="https://fonts.googleapis.com/css2?family=Courier+Prime:wght@700&family=Oswald:wght@500&family=Lato:wght@400&display=swap">
<style>
  :root {
    --wall: #efefef;
    --paper: #ffffff;
    --board: #0e0e0e;
    --board-glow: #1b1b1b;
    --ink: #ffffff;
    --accent: #d52128;
    --item-font: "Courier Prime", "Courier New", monospace;
    --head-font: "Oswald", "Arial Narrow", sans-serif;
    --note-font: "Lato", Arial, sans-serif;
  }
  * { margin: 0; padding: 0; box-sizing: border-box; }
  html, body {
    width: 1200px; height: 1000px; overflow: hidden;
    background: var(--wall);
  }
  .menu-sheet {
    position: absolute; left: 55px; top: 145px;
    width: 1090px; height: 775px;
    background: var(--paper);
  }
  .menu-board {
    position: absolute; left: 72px; top: 160px;
    width: 1058px; height: 745px;
    background: radial-gradient(ellipse at 50% 40%, var(--board-glow), var(--board) 75%);
  }
  .abs { position: absolute; }

  .brand {
    left: 0; width: 1200px; top: 196px;
    display: flex; justify-content: center; align-items: center; gap: 12px;
  }
  .brand-dot {
    width: 34px; height: 34px; border-radius: 50%; background: var(--accent);
  }
  .brand-name {
    font-family: var(--item-font); font-weight: 700; font-size: 26px;
    color: var(--ink); letter-spacing: 0.5px;
  }
  .menu-title {
    left: 0; width: 1200px; top: 288px; text-align: center;
    font-family: var(--item-font); font-weight: 700; font-size: 15px; color: var(--ink);
  }

  .section-frame {
    border: 1.5px solid var(--ink);
  }
  .frame-breakfast { left: 153px; top: 344px; width: 428px; height: 284px; }
  .frame-lunch     { left: 623px; top: 344px; width: 427px; height: 284px; }
  .frame-light     { left: 153px; top: 673px; width: 897px; height: 182px; }

  .ribbon { width: 307px; height: 37px; }
  .ribbon svg { position: absolute; left: 0; top: 0; }
  .ribbon-label {
    position: absolute; inset: 0; display: flex; align-items: center; justify-content: center;
    font-family: var(--head-font); font-weight: 500; font-size: 20px;
    color: var(--ink); letter-spacing: 0.3px;
  }
  .ribbon-breakfast { left: 213px; top: 325px; }
  .ribbon-lunch     { left: 683px; top: 325px; }
  .ribbon-light     { left: 213px; top: 654px; }

  .item-list {
    list-style: none;
    font-family: var(--item-font); font-weight: 700; font-size: 16px;
    line-height: 21.5px; color: var(--ink);
  }
  .item-list li { display: flex; justify-content: space-between; white-space: nowrap; }
  .list-breakfast { left: 185px; top: 377px; width: 365px; }
  .list-lunch     { left: 654px; top: 377px; width: 365px; }
  .list-light-a   { left: 185px; top: 711px; width: 365px; }
  .list-light-b   { left: 654px; top: 689px; width: 365px; }

  .contact-note {
    left: 0; width: 1200px; top: 874px; text-align: center;
    font-family: var(--note-font); font-size: 11.5px; color: var(--ink);
  }
</style>
</head>
<body>
  <div class="menu-sheet"></div>
  <div class="menu-board"></div>

  <div class="abs brand">
    <span class="brand-dot"></span>
    <span class="brand-name">Harbour Lane Canteen</span>
  </div>
  <p class="abs menu-title">catering menu</p>

  <div class="abs section-frame frame-breakfast"></div>
  <div class="abs section-frame frame-lunch"></div>
  <div class="abs section-frame frame-light"></div>

  <div class="abs ribbon ribbon-breakfast">
    <svg width="307" height="37" viewBox="0 0 307 37"><polygon points="1,1 306,1 290,18.5 306,36 1,36 17,18.5" fill="#0e0e0e" stroke="#ffffff" stroke-width="1.5"/></svg>
    <span class="ribbon-label">BREAKFAST</span>
  </div>
  <div class="abs ribbon ribbon-lunch">
    <svg width="307" height="37" viewBox="0 0 307 37"><polygon points="1,1 306,1 290,18.5 306,36 1,36 17,18.5" fill="#0e0e0e" stroke="#ffffff" stroke-width="1.5"/></svg>
    <span class="ribbon-label">LUNCH</span>
  </div>
  <div class="abs ribbon ribbon-light">
    <svg width="307" height="37" viewBox="0 0 307 37"><polygon points="1,1 306,1 290,18.5 306,36 1,36 17,18.5" fill="#0e0e0e" stroke="#ffffff" stroke-width="1.5"/></svg>
    <span class="ribbon-label">SOMETHING LIGHT</span>
  </div>

  <ul class="abs item-list list-breakfast">
    <li><span>toast</span><span>$2.0</span></li>
    <li><span>raisin toast</span><span>$2.0</span></li>
    <li><span>egg bacon and cheese roll</span><span>$6.5</span></li>
    <li><span>veggie brekky wrap</span><span>$6.5</span></li>
    <li><span>ham and cheese french toast</span><span>$6.5</span></li>
    <li><span>ham and cheese toastie</span><span>$5.5</span></li>
    <li><span>cheese and tomato toastie</span><span>$5.5</span></li>
    <li><span>ham and cheese croissant</span><span>$6.5</span></li>
    <li><span>cheese and tomato croissant</span><span>$6.0</span></li>
    <li><span>ham cheese and tomato toastie</span><span>$6.0</span></li>
    <li><span>plain croissant</span><span>$3.5</span></li>
  </ul>

  <ul class="abs item-list list-lunch">
    <li><span>pre made sandwiches</span><span>$6.5/$7.5</span></li>
    <li><span>pre made focaccias</span><span>$8.5</span></li>
    <li><span>pre made wraps</span><span>$7.5</span></li>
    <li><span>pre made mini rolls</span><span>$4.0</span></li>
    <li><span>pre made baguettes</span><span>$9.0</span></li>
    <li><span>pre made bagels</span><span>$9.0</span></li>
    <li><span>fresh salads made daily</span><span>$9.5</span></li>
    <li><span>hot chips</span><span>$4.5</span></li>
    <li><span>plain hamburger</span><span>$7.5</span></li>
    <li><span>hamburger with the lot</span><span>$9.0</span></li>
    <li><span>chicken schnitzel burger</span><span>$8.5</span></li>
  </ul>

  <ul class="abs item-list list-light-a">
    <li><span>mixed yoghurts</span><span>$5.5</span></li>
    <li><span>granola and fruit yoghurt</span><span>$5.5</span></li>
    <li><span>chia pudding</span><span>$5.5</span></li>
    <li><span>bircher muesli</span><span>$5.5</span></li>
    <li><span>fruit salad</span><span>$5.5</span></li>
    <li><span>banana bread</span><span>$4.5</span></li>
  </ul>

  <ul class="abs item-list list-light-b">
    <li><span>muffins - made fresh daily</span><span>$4.5</span></li>
    <li><span>slices</span><span>$4.0</span></li>
    <li><span>cookies</span><span>$4.0</span></li>
    <li><span>choc crunch energy bite</span><span>$4.0</span></li>
    <li><span>super crunch energy bite</span><span>$4.0</span></li>
    <li><span>chocolate bar</span><span>$3.0</span></li>
    <li><span>packet of chips</span><span>$3.0</span></li>
  </ul>

  <p class="abs contact-note">Visit us instore to discuss catering options, or call 0400 218 604 or email jo@harbourlanecanteen.com</p>
</body>
</html>
```